Business Card Design (NEW FILES)

ATTENTION: New vector files are available. Please update your design to reflect/use the new (better resolution) logo images.

Seeking a unique and professional business card design for a commercial drone photography/videography business. The layout should feature
the logo (attached) and include the following information:
Pete Varner
978-552-6170
www.skylarkvisuals.example
NVR Certified Remote Pilot

Pete Varner

```html
<!DOCTYPE html>
<html lang="en">
<head>
<meta charset="utf-8">
<title>Skylark Visuals – Business Card</title>
<link rel="stylesheet" href="https://fonts.googleapis.com/css2?family=Montserrat:wght@400;500;800&display=swap">
<style>
  :root {
    --backdrop: #c9c9c9;
    --navy: #262a52;
    --navy-deep: #1e2147;
    --navy-light: #353a66;
    --paper: #ffffff;
    --accent: #e8935a;
    --ink: #23264d;
  }
  * { box-sizing: border-box; margin: 0; padding: 0; }
  html, body {
    width: 1200px; height: 900px; overflow: hidden;
    background: var(--backdrop);
    font-family: "Montserrat", Arial, sans-serif;
  }
  .canvas { position: relative; width: 1200px; height: 900px; }

  .card {
    position: absolute;
    width: 700px; height: 400px;
    border-radius: 34px;
    box-shadow: 0 6px 14px rgba(0,0,0,0.18);
  }
  .card--front {
    left: 110px; top: 40px;
    background: linear-gradient(160deg, var(--navy) 0%, var(--navy-deep) 55%, var(--navy-light) 100%);
    display: flex; align-items: center; justify-content: center;
  }
  .card--back {
    left: 390px; top: 460px;
    background: var(--paper);
  }

  .brand {
    display: flex; align-items: center; gap: 16px;
  }
  .brand__dot {
    width: 34px; height: 34px; border-radius: 50%;
    background: var(--accent);
    flex-shrink: 0;
  }
  .brand__name {
    font-weight: 500;
    letter-spacing: 2px;
    text-transform: uppercase;
  }
  .card--front .brand__name { color: var(--paper); font-size: 40px; }
  .card--back .brand {
    position: absolute; right: 60px; top: 95px;
  }
  .card--back .brand__dot { width: 26px; height: 26px; }
  .card--back .brand__name { color: var(--ink); font-size: 28px; }

  .person {
    position: absolute; left: 58px; top: 190px;
    color: var(--ink);
  }
  .person__name { font-weight: 800; font-size: 26px; }
  .person__role { font-weight: 400; font-size: 15px; margin-top: 2px; }

  .credentials {
    position: absolute; left: 200px; top: 250px;
    color: var(--ink); font-size: 15px; line-height: 1.25;
  }

  .contact {
    position: absolute; left: 205px; top: 305px;
    list-style: none; color: var(--ink); font-size: 15px;
  }
  .contact__item { display: flex; align-items: center; gap: 12px; line-height: 1.35; }
  .contact__icon { width: 13px; height: 13px; fill: var(--ink); flex-shrink: 0; }
</style>
</head>
<body>
<main class="canvas">

  <section class="card card--front" aria-label="Card front">
    <div class="brand">
      <span class="brand__dot"></span>
      <span class="brand__name">Skylark Visuals</span>
    </div>
  </section>

  <section class="card card--back" aria-label="Card back">
    <div class="brand">
      <span class="brand__dot"></span>
      <span class="brand__name">Skylark Visuals</span>
    </div>

    <div class="person">
      <p class="person__name">Pete Varner</p>
      <p class="person__role">Owner</p>
    </div>

    <div class="credentials">
      <p>NVR Certified Remote Pilot</p>
      <p>Fully Insured</p>
    </div>

    <ul class="contact">
      <li class="contact__item">
        <svg class="contact__icon" viewBox="0 0 16 16" aria-hidden="true"><path d="M3 1h3l1.5 4-2 1.3a9 9 0 0 0 4.2 4.2L11 8.5l4 1.5v3a2 2 0 0 1-2 2A12 12 0 0 1 1 3a2 2 0 0 1 2-2z"/></svg>
        <span>978-552-6170</span>
      </li>
      <li class="contact__item">
        <svg class="contact__icon" viewBox="0 0 16 16" aria-hidden="true"><path d="M1 3h14v10H1z M1.5 3.5 8 9l6.5-5.5" stroke="#fff" stroke-width="1.2"/></svg>
        <span>info@skylarkvisuals.example</span>
      </li>
      <li class="contact__item">
        <svg class="contact__icon" viewBox="0 0 16 16" aria-hidden="true"><circle cx="8" cy="8" r="7"/><path d="M1 8h14M8 1c-3 3-3 11 0 14M8 1c3 3 3 11 0 14" stroke="#fff" stroke-width="1" fill="none"/></svg>
        <span>www.skylarkvisuals.example</span>
      </li>
    </ul>
  </section>

</main>
</body>
</html>
```